Plastic Aesthetic and Reconstructive Surgery

I need a double sided luxurius Business Card, with a minimal, modern design focused on my job.
Besides my Name, Surname and contact information, the use of my initials (M and T) in free style combination as a logo will help.
In the one side all data written in English.
In the other side written in Greek if possible.
Please feel free to use the letter type and size you prefer.
Please use icons type and size and orientation you like.
The Name, Surname, occupation and the initials can be UV spotted.
You can use also in the background a texture or something that will make the card luxurious.
I would prefer pal colors.
Each side can have different colors or even better they can be reversed or inverted
As I have said you can use the wet sand color, light brown, dark brown, gold, light gold, white
Updates

Need extra days to review

i am waiting for some new ideas and some modifications from the designers. I need a couple of days extention of the period for the designers to post their modifications.

Target Market(s)

Patients who need a reconstructive intervention or surgery. Also people, mainly women, that they need aesthetic or cosmetic interventions to face or body

Contact Information for Business Card

Name and surname, occupation, member of an organization , mobile telephone number, Mail, Facebook and Instagram accounts

Font styles to use
Script
Other font styles liked:
• Gabriola

Colors
FFC000
F8CF3A
FAE287
FDF2CF
FEFAEE

Requirements
Must have
• A free combination of my initials (M and T) as a logo
Nice to have
• Fade out with the background colors, UV spotted of the name, initials logo
Should not have
• Address

```html
<!DOCTYPE html>
<html lang="en">
<head>
<meta charset="utf-8">
<title>Markos Theodorou – Business Card</title>
<link rel="stylesheet" href="https://fonts.googleapis.com/css2?family=Raleway:wght@500;800&family=Manrope:wght@500;700&family=Noto+Sans:wght@400;700&display=swap">
<style>
  :root {
    --backdrop: #a57a5e;
    --sand: #c29670;
    --light-sand: #d6b896;
    --deep: #a57a5e;
    --white: #ffffff;
  }
  * { margin: 0; padding: 0; box-sizing: border-box; }
  html, body { width: 1200px; height: 1200px; overflow: hidden; }
  body { background: var(--backdrop); position: relative; font-family: "Raleway", sans-serif; }

  .card {
    position: absolute; left: 186px; width: 835px; height: 477px;
    border-radius: 31px; overflow: hidden;
    box-shadow: 0 8px 18px rgba(60, 35, 20, 0.35);
  }
  .card--front { top: 88px; background: var(--sand); }
  .card--back { top: 643px; background: var(--white); }

  .band { position: absolute; left: 0; right: 0; bottom: 0; height: 48px; }
  .card--front .band { background: var(--light-sand); }
  .card--back .band { background: var(--sand); }

  .rule { position: absolute; top: 180px; height: 11px; background: var(--light-sand); }
  .rule--left { left: 0; width: 296px; }
  .rule--right { right: 0; width: 296px; }

  .monogram {
    position: absolute; border-radius: 50%; background: var(--deep);
    display: flex; align-items: center; justify-content: center;
    font-family: "Raleway", sans-serif; font-weight: 500; color: var(--light-sand);
  }
  .card--front .monogram { left: 334px; top: 107px; width: 166px; height: 166px; font-size: 86px; }
  .card--back .monogram { left: 680px; top: 262px; width: 106px; height: 106px; font-size: 54px; }

  .front-name {
    position: absolute; left: 0; right: 0; top: 308px; text-align: center;
    color: var(--white); font-weight: 800; font-size: 30px; letter-spacing: 2.2px;
  }
  .front-role {
    position: absolute; left: 0; right: 0; top: 349px; text-align: center;
    color: var(--white); font-weight: 500; font-size: 22px; letter-spacing: 2px;
  }

  .greek { font-family: "Noto Sans", sans-serif; color: var(--sand); position: absolute; left: 50px; }
  .greek-name { top: 59px; font-size: 30px; letter-spacing: 3px; white-space: nowrap; }
  .greek-name .degrees { font-family: "Raleway", sans-serif; font-weight: 800; letter-spacing: 2.5px; }
  .greek-role { top: 106px; font-size: 21px; letter-spacing: 2.4px; }
  .greek-member { top: 144px; font-size: 21px; letter-spacing: 2.4px; }

  .contact { position: absolute; display: flex; gap: 9px; font-family: "Manrope", sans-serif; color: var(--sand); }
  .contact__icon {
    width: 46px; height: 46px; border-radius: 50%; background: var(--sand); flex: none;
    display: flex; align-items: center; justify-content: center;
  }
  .contact__label { font-weight: 700; font-size: 16px; line-height: 20px; margin-top: 2px; }
  .contact__value { font-weight: 500; font-size: 16px; line-height: 21px; letter-spacing: 2px; }
  .contact--social { left: 49px; top: 218px; }
  .contact--mail { left: 364px; top: 218px; }
  .contact--photo { left: 49px; top: 323px; }
  .contact--phone { left: 364px; top: 323px; }
</style>
</head>
<body>

<section class="card card--front">
  <div class="rule rule--left"></div>
  <div class="rule rule--right"></div>
  <div class="monogram">MT</div>
  <p class="front-name">Markos Theodorou, MD, MSc</p>
  <p class="front-role">Plastic Reconstructive and Aesthetic Surgery</p>
  <div class="band"></div>
</section>

<section class="card card--back" lang="el">
  <p class="greek greek-name">Μάρκος Θεοδώρου<span class="degrees">, MD, MSc</span></p>
  <p class="greek greek-role">Αισθητική και Επανορθωτική Πλαστική Χειρουργική</p>
  <p class="greek greek-member">Χειρουργική Μέλος Ε.Λ.Ε.Π.Χ</p>

  <div class="contact contact--social" lang="en">
    <div class="contact__icon"></div>
    <div><p class="contact__label">Social Page</p><p class="contact__value">Your address Here</p></div>
  </div>

  <div class="contact contact--mail" lang="en">
    <div class="contact__icon">
      <svg width="26" height="20" viewBox="0 0 26 20" aria-hidden="true">
        <rect x="1.5" y="1.5" width="23" height="17" rx="4" fill="none" stroke="#fff" stroke-width="2.4"/>
        <path d="M3 4 L13 12 L23 4" fill="none" stroke="#fff" stroke-width="2.4" stroke-linejoin="round"/>
      </svg>
    </div>
    <div><p class="contact__label">Email Address</p><p class="contact__value">m.theodorou27<br>@mailpost.gr</p></div>
  </div>

  <div class="contact contact--photo" lang="en">
    <div class="contact__icon"></div>
    <div><p class="contact__label">Photo Profile</p><p class="contact__value">www.theodorou-clinic.gr</p></div>
  </div>

  <div class="contact contact--phone" lang="en">
    <div class="contact__icon">
      <svg width="24" height="24" viewBox="0 0 24 24" aria-hidden="true">
        <path fill="#fff" d="M6.6 10.8a15.1 15.1 0 0 0 6.6 6.6l2.2-2.2a1 1 0 0 1 1-.25 11.4 11.4 0 0 0 3.6.57 1 1 0 0 1 1 1V20a1 1 0 0 1-1 1A17 17 0 0 1 3 4a1 1 0 0 1 1-1h3.5a1 1 0 0 1 1 1c0 1.25.2 2.45.57 3.57a1 1 0 0 1-.25 1z"/>
      </svg>
    </div>
    <div><p class="contact__label">Office Number</p><p class="contact__value">+30 690 412 3386</p></div>
  </div>

  <div class="monogram">MT</div>
  <div class="band"></div>
</section>

</body>
</html>
```